Spring Savings Package for The Lodge at Harlan's Meadow Lodge

Design an email and elevator poster 11x7 that promotes Spring and our heated pools at The Lodge at Harlan's Meadow
Text-

Worried about the Spring Weather don't #IndoorWaterpark !

Ask about our Springtime Savings that comes with a Free Resort Beach Towel ($12 value).

Book by March 1st,2019
Stay Dates Now-May 23rd,2019

Phone number: 800.555.0192

Reserve Now! www (dot) lodgeatharlansmeadow (dot) com

Target Market(s)

Guest reserving Spring Break

Industry/Entity Type

Hospitality

Requirements
Must have
• text
• phone
• website
• Book Now
• Can change some of the text to make it more of a Sales piece
Nice to have
• Brand Colors

```html
<!DOCTYPE html>
<html lang="en">
<head>
<meta charset="UTF-8">
<title>Springtime Savings – The Lodge at Harlan's Meadow</title>
<link rel="stylesheet" href="https://fonts.googleapis.com/css2?family=Oswald:wght@300;400;600;700&family=Poppins:wght@400;600;700&display=swap">
<style>
  :root {
    --backdrop: #c3dcf2;
    --paper: #ffffff;
    --deep-blue: #1a4fc6;
    --mid-blue: #1e68d6;
    --sky-blue: #16a3e3;
    --aqua: #0fbbe6;
    --ink: #1c1c1c;
    --glow: #f2d51c;
    --white: #ffffff;
  }
  * { box-sizing: border-box; margin: 0; padding: 0; }
  html, body {
    width: 1200px; height: 840px; overflow: hidden;
    background: var(--backdrop);
  }
  .canvas {
    position: relative; width: 1200px; height: 840px;
    display: flex; align-items: center; justify-content: center;
  }
  .poster {
    position: relative; width: 560px; height: 794px; overflow: hidden;
    background: linear-gradient(180deg, var(--deep-blue) 0%, var(--mid-blue) 32%, var(--sky-blue) 58%, var(--aqua) 100%);
    color: var(--white);
    font-family: 'Oswald', sans-serif;
  }
  .poster__shapes { position: absolute; inset: 0; }
  .brand {
    position: absolute; display: flex; align-items: center; gap: 8px;
    font-family: 'Poppins', sans-serif; font-weight: 600; line-height: 1;
  }
  .brand--resort { left: 32px; top: 50px; color: var(--ink); font-size: 24px; }
  .brand--resort .brand__dot {
    width: 12px; height: 12px; border-radius: 50%; background: var(--glow);
  }
  .brand--park { right: 28px; top: 46px; color: var(--mid-blue); font-size: 30px; font-weight: 700; }
  .headline {
    position: absolute; left: 29px; top: 242px;
    font-weight: 700; font-size: 34px; line-height: 1.13; letter-spacing: 0.2px;
  }
  .hashtag {
    position: absolute; left: 29px; top: 323px;
    font-family: 'Poppins', sans-serif; font-weight: 600; font-size: 16px;
  }
  .offer { position: absolute; left: 27px; top: 0; width: 100%; }
  .offer__lead { position: absolute; top: 424px; left: 2px; font-weight: 600; font-size: 21px; }
  .offer__title { position: absolute; top: 450px; left: 0; font-weight: 700; font-size: 44px; letter-spacing: 0.3px; white-space: nowrap; }
  .offer__bridge { position: absolute; top: 500px; left: 212px; font-weight: 300; font-size: 19px; }
  .offer__gift { position: absolute; top: 525px; left: 0; font-weight: 700; font-size: 42px; letter-spacing: 0.3px; white-space: nowrap; }
  .badge {
    position: absolute; left: 431px; top: 361px; width: 132px; height: 132px;
    color: var(--deep-blue); text-align: center; font-weight: 700;
  }
  .badge__amount { position: absolute; top: 18px; left: 22px; font-size: 58px; line-height: 1; }
  .badge__currency { font-size: 22px; vertical-align: 6px; margin-right: 1px; }
  .badge__label {
    position: absolute; top: 80px; left: 40px;
    font-family: 'Poppins', sans-serif; font-size: 20px; line-height: 1;
  }
  .details {
    position: absolute; left: 25px; right: 20px; top: 666px;
    display: flex; align-items: stretch;
    font-family: 'Poppins', sans-serif; font-weight: 600; font-size: 13.5px; line-height: 1.2;
    text-transform: uppercase;
  }
  .details__item { padding-right: 22px; }
  .details__item + .details__item { border-left: 1.5px solid var(--white); padding-left: 22px; }
  .details__item:nth-child(1) { width: 151px; }
  .details__item:nth-child(2) { width: 208px; }
  .website {
    position: absolute; left: 0; right: 0; top: 729px; text-align: center;
    font-family: 'Poppins', sans-serif; font-weight: 600; font-size: 11.5px;
  }
</style>
</head>
<body>
<main class="canvas">
  <article class="poster">
    <svg class="poster__shapes" width="560" height="794" viewBox="0 0 560 794" aria-hidden="true">
      <path d="M0 0 H560 V168 C430 160 270 140 202 77 C150 120 70 145 0 152 Z" fill="var(--paper)"/>
      <path d="M0 172 C70 165 140 140 196 98" fill="none" stroke="var(--white)" stroke-width="1.5"/>
      <path d="M236 118 C320 162 440 176 560 180" fill="none" stroke="var(--white)" stroke-width="1.5"/>
      <circle cx="497" cy="427" r="74" fill="none" stroke="var(--white)" stroke-width="1.5"/>
      <circle cx="497" cy="427" r="66" fill="var(--white)"/>
    </svg>

    <div class="brand brand--resort"><span class="brand__dot"></span><span>Lantern Bay</span></div>
    <div class="brand brand--park">Splash Harbor</div>

    <h1 class="headline">WORRIED ABOUT<br>THE SPRING WEATHER DON'T</h1>
    <p class="hashtag">#IndoorWaterpark !</p>

    <section class="offer">
      <p class="offer__lead">ASK ABOUT OUR</p>
      <h2 class="offer__title">SPRINGTIME SAVINGS</h2>
      <p class="offer__bridge">THAT COMES WITH A</p>
      <h2 class="offer__gift">FREE RESORT BEACH TOWEL</h2>
    </section>

    <div class="badge">
      <div class="badge__amount"><span class="badge__currency">$</span>12</div>
      <div class="badge__label">value</div>
    </div>

    <div class="details">
      <div class="details__item">Book by March<br>1st,2019</div>
      <div class="details__item">Stay Dates<br>Now-May 23rd,2019</div>
      <div class="details__item">Phone Number:<br>800.555.0192</div>
    </div>

    <p class="website">www.lodgeatharlansmeadow.com</p>
  </article>
</main>
</body>
</html>
```